Book Cover - For Best Selling Diet

Hi
Book cover required for a diet book being marketed to become a best seller
For best quality, image will be 2820 pixels on the shortest side and 4500 pixels on the longest side .
The book name : Bright Morning Plan
By Corinna Plett
( will add in the extra text once we see design - top and bottom subtitle )
I do not want a photo of a person on the book.
PLEASE SEE " THE 9 STEP FRAME" by Ned Galbury as an example of solid style and I also love Quiet Ledger for the font.
Branding Colours:
#F26432
#A4195C
#A7D8CC
Font that runs through our brand is : helvetica neue
This is for a book that will be marketed for #1 bestseller - So please only quality
designs that are designed in a unique style.
Thanks
Target Market(s)
Busy Working Mums, Affluent, 30+ .
Look and feel

```html
<!DOCTYPE html>
<html lang="en">
<head>
<meta charset="utf-8">
<title>Bright Morning Plan — Corinna Plett</title>
<link rel="stylesheet" href="https://fonts.googleapis.com/css2?family=Work+Sans:wght@200&display=swap">
<style>
  :root {
    --berry: #a41a5e;
    --rose: #b7435f;
    --coral: #d5654c;
    --ember: #dc6a44;
    --sage: #bfc0a3;
    --ink-light: #ffffff;
    --figure-soft: #f2b8b0;
    --figure-deep: #e0897c;
  }
  html, body {
    margin: 0;
    padding: 0;
    width: 752px;
    height: 1200px;
    overflow: hidden;
  }
  .cover {
    position: relative;
    width: 752px;
    height: 1200px;
    overflow: hidden;
    background:
      radial-gradient(ellipse 420px 360px at 100% 100%, var(--sage) 0%, rgba(191,192,163,0.55) 35%, rgba(191,192,163,0) 75%),
      linear-gradient(168deg, var(--berry) 0%, #ab2a5e 25%, var(--rose) 45%, var(--coral) 72%, var(--ember) 100%);
    font-family: "Work Sans", "Helvetica Neue", Helvetica, Arial, sans-serif;
    color: var(--ink-light);
  }
  .cover__title {
    position: absolute;
    top: 96px;
    left: 0;
    width: 100%;
    margin: 0;
    text-align: center;
    font-weight: 200;
    font-size: 118px;
    line-height: 128px;
    letter-spacing: 1px;
    text-transform: uppercase;
  }
  .cover__title span { display: block; }
  .cover__figure {
    position: absolute;
    left: 252px;
    top: 540px;
    width: 264px;
    height: 498px;
  }
  .cover__author {
    position: absolute;
    top: 1064px;
    left: 0;
    width: 100%;
    margin: 0;
    text-align: center;
    font-weight: 200;
    font-size: 72px;
    line-height: 88px;
    letter-spacing: 1px;
    text-transform: uppercase;
  }
</style>
</head>
<body>
  <main class="cover">
    <h1 class="cover__title">
      <span>Bright</span>
      <span>Morning</span>
      <span>Plan</span>
    </h1>

    <svg class="cover__figure" viewBox="0 0 264 498" role="img" aria-label="Soft translucent silhouette illustration of a standing woman, one hand raised to her head">
      <defs>
        <linearGradient id="figureTone" x1="0" y1="0" x2="0" y2="1">
          <stop offset="0" stop-color="var(--figure-soft)" stop-opacity="0.55"/>
          <stop offset="1" stop-color="var(--figure-deep)" stop-opacity="0.6"/>
        </linearGradient>
      </defs>
      <rect x="0" y="0" width="264" height="498" rx="120" fill="url(#figureTone)"/>
    </svg>

    <p class="cover__author">Corinna Plett</p>
  </main>
</body>
</html>
```